Aviation Banner Ad Designs

SkyLedgerMetrics provides access to the most accurate aircraft operating cost information, to compare Piston, Turboprop and Jet aircraft.

The banners ads will be used for retargeting/remarketing - to bring visitors back to the site. The banners should remind and reinforce the key messages of what the site provides.

Target Market(s)

Private aircraft buyers including:
- Aircraft Brokers
- Charter Operators
- Corporate Flight Departments
- Aircraft Management companies
- Financial Institutions
- Aircraft Owners
- Prospective Buyers

Requirements
Must have
• A. Banner Objective
The visual and textual content of the banner should remind the viewer about the features of the site, and prompt them to return to the site.
1. Arresting visual
2. Headline
3. Single message
4. Compelling CTA
5. Logo - big enough to see
6. Standard IAB ad sizes/specs

B. Design Elements
Logo: As attached
Main Title: Calculate Jet Operating Costs
Subtitle: Compare Ownership Usage Scenarios
Call to Action Button: Compare Ownership Costs
Background: Several images supplied as options

C. Banner Sizes
Do examples as 300×250 , 728×90 , 160×600
Final sizes to also include 320×100 , 336x280 , 300x600

Finally delivery as .jpg files.

Font - use same font as on site

```html
<!DOCTYPE html>
<html lang="en">
<head>
<meta charset="utf-8">
<title>SkyLedgerMetrics – Banner Set</title>
<link rel="stylesheet" href="https://fonts.googleapis.com/css2?family=Oswald:wght@500&family=Roboto:wght@400;500&display=swap">
<style>
  :root{
    --canvas:#d8d8d8;
    --label:#9a9a9a;
    --navy:#1f3a78;
    --navy-deep:#142a5c;
    --red:#d3222a;
    --white:#ffffff;
    --sky:#6f93c4;
    --fuselage:#d9cfb6;
  }
  html,body{margin:0;padding:0;overflow:hidden;background:var(--canvas);}
  .canvas{position:relative;width:1200px;height:1181px;overflow:hidden;background:var(--canvas);}
  .stage{position:absolute;left:0;top:0;width:1139px;height:1121px;transform:scale(1.0536);transform-origin:0 0;}
  .size-label{position:absolute;font:400 16px "Roboto",sans-serif;color:var(--label);letter-spacing:.5px;}
  .banner{position:absolute;overflow:hidden;background:var(--navy);box-shadow:4px 6px 8px rgba(0,0,0,.28);}
  .banner-art{position:absolute;left:0;top:0;width:100%;height:100%;display:block;}
  .headline{position:absolute;margin:0;font-family:"Oswald",sans-serif;font-weight:500;color:var(--white);text-transform:uppercase;line-height:1.15;white-space:nowrap;}
  .subline{position:absolute;margin:0;font-family:"Roboto",sans-serif;color:var(--white);letter-spacing:.4px;line-height:1.35;white-space:nowrap;}
  .cta{position:absolute;display:flex;align-items:center;justify-content:center;text-align:center;background:var(--red);color:var(--white);font-family:"Roboto",sans-serif;font-weight:500;line-height:1.25;border-radius:999px;letter-spacing:.3px;}
  .cta--tab{border-radius:999px 0 0 999px;}
  .brand{position:absolute;display:flex;align-items:center;gap:4px;font-family:"Roboto",sans-serif;font-weight:500;color:var(--navy-deep);letter-spacing:.3px;white-space:nowrap;}
  .brand-mark{display:block;background:var(--red);flex:none;}
  .center{text-align:center;left:0;right:0;}
</style>
</head>
<body>
<div class="canvas">
<div class="stage">

  <svg width="0" height="0" style="position:absolute">
    <defs>
      <linearGradient id="photoJet" x1="0" y1="0" x2="1" y2="1">
        <stop offset="0" stop-color="#e4dcc6"/>
        <stop offset=".45" stop-color="#c9bd9d"/>
        <stop offset="1" stop-color="#6f93c4"/>
      </linearGradient>
      <linearGradient id="photoTail" x1="0" y1="0" x2="0" y2="1">
        <stop offset="0" stop-color="#24427f"/>
        <stop offset=".6" stop-color="#1c3670"/>
        <stop offset="1" stop-color="#132a5a"/>
      </linearGradient>
    </defs>
  </svg>

  <!-- 320 x 100 -->
  <span class="size-label" style="left:97px;top:65px">320 × 100</span>
  <div class="banner" style="left:96px;top:90px;width:320px;height:101px">
    <svg class="banner-art" viewBox="0 0 320 101" preserveAspectRatio="none">
      <rect width="320" height="101" fill="url(#photoTail)" role="img" aria-label="Navy-tinted view of a private jet tail"/>
      <path d="M0,0 H150 C110,30 60,50 0,58 Z" fill="url(#photoJet)" role="img" aria-label="Private jet with open door and engine"/>
      <path d="M0,58 C60,50 110,30 150,0 H158 C118,36 62,64 0,74 Z" fill="var(--red)"/>
      <path d="M150,0 H158 C118,36 62,64 0,74 V76 C64,66 120,38 162,0 Z" fill="var(--white)"/>
      <path d="M200,101 C222,76 258,64 320,62 V68 C262,70 228,80 208,101 Z" fill="var(--red)"/>
      <path d="M208,101 C228,80 262,70 320,68 V101 Z" fill="var(--white)"/>
    </svg>
    <h2 class="headline" style="left:120px;top:23px;font-size:15px">Calculate Jet<br>Operating Costs</h2>
    <p class="subline" style="left:120px;top:62px;font-size:8.5px">Compare Ownership<br>Usage Scenarios</p>
    <div class="cta cta--tab" style="left:230px;top:10px;width:90px;height:30px;font-size:8px">Compare<br>Ownership Costs</div>
    <div class="brand" style="left:240px;top:78px;font-size:6.5px"><span class="brand-mark" style="width:7px;height:7px"></span>SkyLedgerMetrics</div>
  </div>

  <!-- 728 x 90 -->
  <span class="size-label" style="left:97px;top:238px">728 x 90</span>
  <div class="banner" style="left:96px;top:263px;width:728px;height:90px">
    <svg class="banner-art" viewBox="0 0 728 90" preserveAspectRatio="none">
      <rect width="728" height="90" fill="url(#photoTail)" role="img" aria-label="Navy-tinted view of a private jet tail"/>
      <path d="M0,0 H222 C170,38 90,66 0,72 Z" fill="url(#photoJet)" role="img" aria-label="Private jet with open door and engine"/>
      <path d="M0,72 C90,66 170,38 222,0 H234 C176,44 96,78 0,86 Z" fill="var(--red)"/>
      <path d="M222,0 H234 C176,44 96,78 0,86 V89 C98,81 180,46 240,0 Z" fill="var(--white)"/>
      <path d="M558,90 C590,40 650,22 728,20 V27 C654,29 600,46 568,90 Z" fill="var(--red)"/>
      <path d="M568,90 C600,46 654,29 728,27 V90 Z" fill="var(--white)"/>
    </svg>
    <h2 class="headline" style="left:200px;top:24px;font-size:18px">Calculate Jet Operating Costs</h2>
    <p class="subline" style="left:200px;top:48px;font-size:11px">Compare Ownership Usage Scenarios</p>
    <div class="cta" style="left:461px;top:25px;width:110px;height:40px;font-size:9.5px">Compare<br>Ownership Costs</div>
    <div class="brand" style="left:620px;top:52px;font-size:8.5px"><span class="brand-mark" style="width:9px;height:9px"></span>SkyLedgerMetrics</div>
  </div>

  <!-- 300 x 600 -->
  <span class="size-label" style="left:97px;top:392px">300 x 600</span>
  <div class="banner" style="left:96px;top:417px;width:300px;height:600px">
    <svg class="banner-art" viewBox="0 0 300 600" preserveAspectRatio="none">
      <rect width="300" height="600" fill="url(#photoTail)" role="img" aria-label="Navy-tinted view of a private jet tail over clouds"/>
      <path d="M0,0 H300 V112 C210,160 100,190 0,168 Z" fill="url(#photoJet)" role="img" aria-label="Private jet with open door, stairs and engine"/>
      <path d="M0,168 C100,190 210,160 300,112 V122 C210,178 90,214 0,196 Z" fill="var(--red)"/>
      <path d="M300,122 C210,178 90,214 0,196 V202 C90,220 212,184 300,127 Z" fill="var(--white)"/>
      <path d="M0,508 C100,474 200,474 300,508 V518 C200,486 100,486 0,518 Z" fill="var(--red)"/>
      <path d="M0,518 C100,486 200,486 300,518 V600 H0 Z" fill="var(--white)"/>
    </svg>
    <h2 class="headline center" style="top:242px;font-size:32px;line-height:1.17">Calculate Jet<br>Operating Costs</h2>
    <p class="subline center" style="top:333px;font-size:14px;line-height:1.65">Compare Ownership Usage<br>Scenarios</p>
    <div class="cta" style="left:43px;top:395px;width:224px;height:44px;font-size:13px">Compare Ownership Costs</div>
    <div class="brand" style="left:70px;top:538px;font-size:15px"><span class="brand-mark" style="width:16px;height:16px"></span>SkyLedgerMetrics</div>
  </div>

  <!-- 160 x 600 -->
  <span class="size-label" style="left:469px;top:392px">160 x 600</span>
  <div class="banner" style="left:472px;top:417px;width:160px;height:600px">
    <svg class="banner-art" viewBox="0 0 160 600" preserveAspectRatio="none">
      <rect width="160" height="600" fill="url(#photoTail)" role="img" aria-label="Navy-tinted view of a private jet tail over clouds"/>
      <path d="M0,0 H160 V120 C110,150 50,168 0,160 Z" fill="url(#photoJet)" role="img" aria-label="Private jet with open door, stairs and engine"/>
      <path d="M0,160 C50,168 110,150 160,120 V130 C110,166 50,186 0,178 Z" fill="var(--red)"/>
      <path d="M160,130 C110,166 50,186 0,178 V183 C50,191 112,172 160,135 Z" fill="var(--white)"/>
      <path d="M0,500 C50,482 110,482 160,500 V510 C110,494 50,494 0,510 Z" fill="var(--red)"/>
      <path d="M0,510 C50,494 110,494 160,510 V600 H0 Z" fill="var(--white)"/>
    </svg>
    <h2 class="headline center" style="top:228px;font-size:24px;line-height:1.15">Calculate<br>Jet Operating<br>Costs</h2>
    <p class="subline center" style="top:326px;font-size:13px;line-height:1.4">Compare Ownership<br>Usage Scenarios</p>
    <div class="cta" style="left:18px;top:394px;width:126px;height:44px;font-size:11px">Compare<br>Ownership Costs</div>
    <div class="brand" style="left:18px;top:542px;font-size:12px"><span class="brand-mark" style="width:12px;height:12px"></span>SkyLedgerMetrics</div>
  </div>

  <!-- 336 x 280 -->
  <span class="size-label" style="left:707px;top:392px">336 x 280</span>
  <div class="banner" style="left:707px;top:417px;width:336px;height:280px">
    <svg class="banner-art" viewBox="0 0 336 280" preserveAspectRatio="none">
      <rect width="336" height="280" fill="url(#photoTail)" role="img" aria-label="Navy-tinted view of a private jet tail"/>
      <path d="M0,0 H312 C240,50 120,78 0,64 Z" fill="url(#photoJet)" role="img" aria-label="Private jet with open door and engine"/>
      <path d="M0,64 C120,78 240,50 312,0 H326 C250,62 120,98 0,86 Z" fill="var(--red)"/>
      <path d="M326,0 C250,62 120,98 0,86 V90 C120,102 254,66 332,0 Z" fill="var(--white)"/>
      <path d="M0,250 C90,222 240,218 336,244 V254 C240,230 90,234 0,262 Z" fill="var(--red)"/>
      <path d="M0,262 C90,234 240,230 336,254 V280 H0 Z" fill="var(--white)"/>
    </svg>
    <h2 class="headline center" style="top:106px;font-size:23px;line-height:1.2">Calculate Jet<br>Operating Costs</h2>
    <p class="subline center" style="top:170px;font-size:12.5px;line-height:1.25">Compare Ownership Usage<br>Scenarios</p>
    <div class="cta cta--tab" style="left:229px;top:52px;width:107px;height:38px;font-size:9.5px">Compare<br>Ownership Costs</div>
    <div class="brand" style="left:122px;top:250px;font-size:8.5px"><span class="brand-mark" style="width:9px;height:9px"></span>SkyLedgerMetrics</div>
  </div>

  <!-- 300 x 250 -->
  <span class="size-label" style="left:707px;top:742px">300 x 250</span>
  <div class="banner" style="left:707px;top:767px;width:300px;height:250px">
    <svg class="banner-art" viewBox="0 0 300 250" preserveAspectRatio="none">
      <rect width="300" height="250" fill="url(#photoTail)" role="img" aria-label="Navy-tinted view of a private jet tail"/>
      <path d="M0,0 H262 C200,44 100,68 0,54 Z" fill="url(#photoJet)" role="img" aria-label="Private jet with open door and engine"/>
      <path d="M0,54 C100,68 200,44 262,0 H276 C210,54 100,86 0,76 Z" fill="var(--red)"/>
      <path d="M276,0 C210,54 100,86 0,76 V80 C102,90 214,58 282,0 Z" fill="var(--white)"/>
      <path d="M0,226 C80,204 220,200 300,222 V232 C220,212 80,214 0,236 Z" fill="var(--red)"/>
      <path d="M0,236 C80,214 220,212 300,232 V250 H0 Z" fill="var(--white)"/>
    </svg>
    <h2 class="headline center" style="top:90px;font-size:21px;line-height:1.2">Calculate Jet<br>Operating Costs</h2>
    <p class="subline center" style="top:150px;font-size:12.5px;line-height:1.25">Compare Ownership Usage<br>Scenarios</p>
    <div class="cta cta--tab" style="left:200px;top:42px;width:100px;height:36px;font-size:9.5px">Compare<br>Ownership Costs</div>
    <div class="brand" style="left:112px;top:226px;font-size:8px"><span class="brand-mark" style="width:8px;height:8px"></span>SkyLedgerMetrics</div>
  </div>

</div>
</div>
</body>
</html>
```